Sticker Design for a perfume bottle

We need a sticker designed for our new fragrance line. The sticker is made out of metalic foil paper and can be designed using both flat and raised ink. attached is a design that I really like please create a exact copy of this in AI or CDR format for the basic look, you can also create similar versions using Meander Art (greek design patterns) be creative. This is my first perfume line and I would like it to look unique and MODERN . There are two basic styles which i will be choosing from, sticker 1 file & sticker 2 file. Please first recreate them and than add Meander art to them. They will be used for both men and women fragrances.

Please make sure to mark the raised and embossed, flat parts of the graphic.

Requirements
Must have
• Colors are GOLD & SILVER
Nice to have
• Greek patterns similar to lorvanne bottles.

```html
<!DOCTYPE html>
<html lang="en">
<head>
<meta charset="utf-8">
<title>Foil Sticker Design</title>
<link rel="stylesheet" href="https://fonts.googleapis.com/css2?family=Cormorant+Garamond:wght@500&display=swap">
<style>
  :root {
    --backdrop: #e6d9cb;
    --backdrop-edge: #c7af9c;
    --gold-light: #f6d773;
    --gold-mid: #e1ad3a;
    --gold-deep: #c7892a;
    --silver-light: #e4e6e8;
    --silver-mid: #c9cdd1;
    --silver-deep: #aeb3b8;
  }
  html, body {
    margin: 0;
    padding: 0;
    width: 1200px;
    height: 849px;
    overflow: hidden;
    font-family: "Cormorant Garamond", serif;
  }
  .canvas {
    position: relative;
    width: 1200px;
    height: 849px;
    background: radial-gradient(ellipse at center, #f3ece4 0%, var(--backdrop) 45%, var(--backdrop-edge) 100%);
  }
  .sticker {
    position: absolute;
    left: 198px;
    top: 120px;
    width: 804px;
    height: 608px;
    filter: drop-shadow(0 6px 14px rgba(90, 60, 30, 0.18));
  }
</style>
</head>
<body>
<main class="canvas">
  <svg class="sticker" viewBox="0 0 402 304" xmlns="http://www.w3.org/2000/svg" aria-label="Gold and silver foil perfume sticker">
    <defs>
      <linearGradient id="gold-foil" x1="0" y1="0" x2="1" y2="1">
        <stop offset="0" stop-color="var(--gold-deep)"/>
        <stop offset="0.45" stop-color="var(--gold-light)"/>
        <stop offset="1" stop-color="var(--gold-mid)"/>
      </linearGradient>
      <linearGradient id="gold-stripe" x1="0" y1="0" x2="1" y2="0">
        <stop offset="0" stop-color="var(--gold-mid)"/>
        <stop offset="0.5" stop-color="var(--gold-light)"/>
        <stop offset="1" stop-color="var(--gold-deep)"/>
      </linearGradient>
      <linearGradient id="silver-foil" x1="0" y1="0" x2="1" y2="1">
        <stop offset="0" stop-color="var(--silver-deep)"/>
        <stop offset="0.5" stop-color="var(--silver-light)"/>
        <stop offset="1" stop-color="var(--silver-mid)"/>
      </linearGradient>
    </defs>

    <g class="side-band">
      <rect class="band-silver-top" x="0" y="44" width="402" height="38" fill="url(#silver-foil)"/>
      <rect class="band-gold" x="0" y="80" width="402" height="130" fill="url(#gold-stripe)"/>
      <rect class="band-rule" x="0" y="90" width="402" height="3" fill="var(--silver-mid)"/>
      <rect class="band-rule" x="0" y="117" width="402" height="3" fill="var(--silver-mid)"/>
      <rect class="band-rule" x="0" y="142" width="402" height="3" fill="var(--silver-mid)"/>
      <rect class="band-rule" x="0" y="179" width="402" height="3" fill="var(--silver-mid)"/>
      <rect class="band-rule" x="0" y="202" width="402" height="3" fill="var(--silver-mid)"/>
      <rect class="band-silver-bottom" x="0" y="210" width="402" height="42" fill="url(#silver-foil)"/>
    </g>

    <g class="center-panel">
      <rect class="panel-outline" x="50" y="0" width="298" height="304" fill="url(#gold-stripe)"/>
      <rect class="panel-silver" x="54" y="4" width="290" height="296" fill="url(#silver-foil)"/>
      <rect class="meander-border" x="68" y="17" width="267" height="270" fill="url(#gold-foil)"
            role="img" aria-label="Raised gold Greek key meander border"/>
      <rect class="inner-silver" x="87" y="42" width="228" height="225" fill="url(#silver-foil)"/>
      <rect class="foil-center" x="107" y="59" width="188" height="188" fill="url(#gold-foil)"/>
    </g>
  </svg>
</main>
</body>
</html>
```